Personal Injury Mailer for a Chiropractic Office

I need a postcard design for our new Chiropractic office called "Vantrell Chiropractic". I am looking to treat more traumatic injuries such as those caused by auto accidents. I treat using gentle Chiropractic care in combination with Fluid Motion Methods soft tissue massage.

I like some of the elements of the uploaded .jpgs: the smashed car on the one and the lady rubbing her neck and back on the other. I DO NOT like the soft collar neck brace. I would rather the person in the picture be female than male. I am only mailing to potential clients who are not at fault, so I want to communicate to them that their treatment will, in all probability, be at no cost to them. I like the message on the "If you've been in an auto accident, the real damage may not be this obvious" or something to that effect. So many people neglect to get proper treatment after an accident and the effects of these injuries show up down the road.

Please include my headshot (not prominently). Please include "Let us review your case. Schedule a Consult today and receive a FREE tube of Glacivo Pain Reliever ($10 value)." [$10 value in small print] The phrases: "This is an advertisement for chiropractic services." and "If you decide to purchase additional treatment, you have the legal right to change your mind within three days and receive a refund." must be included as disclaimers in small print. They can be place on the address side of the postcard.

I have also included my logo in a few different formats and 3 versions of the FMM/Tidebreaker logo.
(555) 382-7146
www.vantrellchiro-example.com

```html
<!DOCTYPE html>
<html lang="en">
<head>
<meta charset="utf-8">
<title>Vantrell Chiropractic – Personal Injury Mailer</title>
<link rel="stylesheet" href="https://fonts.googleapis.com/css2?family=Arimo:wght@400;700&family=Raleway:wght@400;500;600;700&display=swap">
<style>
  :root {
    --navy: #2b2f8f;
    --royal: #2f3c9e;
    --sky: #3ab4e6;
    --pale-sky: #a9ddf0;
    --alert-red: #e0202a;
    --ink: #333333;
    --rule: #bdbdbd;
    --panel-shadow: rgba(0,0,0,0.18);
    --white: #ffffff;
  }
  * { box-sizing: border-box; margin: 0; padding: 0; }
  html, body { width: 1200px; height: 1000px; overflow: hidden; background: var(--white); }
  .canvas { position: relative; width: 1200px; height: 1000px; }

  .postcard {
    position: absolute; left: 298px; width: 697px;
    background: var(--white);
    box-shadow: 0 3px 8px var(--panel-shadow);
    overflow: hidden;
  }
  .postcard--front { top: 22px; height: 451px; }
  .postcard--back  { top: 522px; height: 453px; }

  .band {
    position: absolute; left: 0;
    background: linear-gradient(90deg, var(--royal) 0%, var(--sky) 100%);
  }

  .side-panel {
    position: absolute; left: 0; top: 0; width: 212px; height: 100%;
    border-right: 3px solid #d6d6d6;
    box-shadow: 2px 0 4px rgba(0,0,0,0.12);
  }

  .brand {
    position: absolute; left: 0; width: 212px; display: flex; align-items: center; justify-content: center; gap: 6px;
    font-family: "Raleway", sans-serif; font-weight: 500; font-variant: small-caps;
    font-size: 15px; color: var(--ink); letter-spacing: 0.2px; white-space: nowrap;
  }
  .brand__dot { width: 13px; height: 13px; border-radius: 50%; background: var(--sky); flex: none; }

  /* Front */
  .headshot {
    position: absolute; left: 45px; top: 138px; width: 130px; height: 182px;
    background: linear-gradient(180deg, #ffffff 0%, #e9e6e2 10%, #c7b9ad 35%, #2a2a2a 62%, #1c1c1c 100%);
    border-radius: 60px 60px 4px 4px;
  }
  .partner-bar {
    position: absolute; left: 0; top: 320px; width: 212px; height: 36px; background: #0b0b0b;
    display: flex; align-items: center; justify-content: space-between; padding: 0 16px 0 8px;
  }
  .partner-badge { height: 18px; border-radius: 3px; }
  .partner-badge--fmm { width: 80px; background: #c8161d; }
  .partner-badge--tide { width: 80px; height: 14px; background: #f2f2f2; }

  .headline {
    position: absolute; left: 214px; top: 20px; width: 483px; text-align: center;
    font-family: "Arimo", sans-serif; font-weight: 700; font-size: 22.5px; line-height: 26px;
    color: var(--navy); text-shadow: 1px 2px 3px rgba(0,0,0,0.25);
  }
  .headline__alert { color: var(--alert-red); }

  .scene {
    position: absolute; left: 216px; top: 100px; width: 481px; height: 220px;
    background: linear-gradient(90deg, #ffffff 0%, #e6e6e6 30%, #d0d0d0 55%, #2c2c34 70%, #24242c 80%, #dcdcdc 92%, #f2f2f2 100%);
  }
  .no-cost {
    position: absolute; left: 228px; top: 112px; width: 200px;
    font-family: "Arimo", sans-serif; font-weight: 700; font-size: 14px; line-height: 18px;
    color: var(--navy);
  }
  .contact-bar {
    position: absolute; left: 214px; top: 320px; width: 483px; height: 36px; background: var(--pale-sky);
    display: flex; align-items: center; justify-content: space-between; padding: 0 16px 0 20px;
    font-family: "Arimo", sans-serif; font-weight: 700; color: var(--navy); white-space: nowrap;
  }
  .contact-bar__phone { font-size: 23px; }
  .contact-bar__web { font-size: 17px; }

  .offer {
    position: absolute; left: 0; top: 356px; width: 697px; height: 95px;
    background: linear-gradient(90deg, var(--royal) 0%, var(--sky) 100%);
    color: var(--white); text-align: center;
    font-family: "Raleway", sans-serif;
  }
  .offer__lead { font-weight: 700; font-size: 22px; line-height: 26px; margin-top: 8px; }
  .offer__line { font-size: 17px; line-height: 23px; font-weight: 500; }
  .offer__small { font-size: 8px; }
  .offer__lead, .offer__line { position: relative; left: 100px; width: 500px; }

  /* Back */
  .disclaimer {
    position: absolute; left: 14px; top: 338px; width: 184px; text-align: center;
    font-family: "Raleway", sans-serif; color: var(--navy);
  }
  .disclaimer__title { font-size: 10.5px; line-height: 13px; font-weight: 500; }
  .disclaimer__body { font-size: 7.5px; line-height: 10px; margin-top: 4px; }

  .watermark {
    position: absolute; left: 240px; top: 150px;
    font-family: "Raleway", sans-serif; font-weight: 500; font-variant: small-caps;
    font-size: 40px; line-height: 48px; color: #e6e9f4;
  }
  .stamp-box {
    position: absolute; left: 590px; top: 13px; width: 104px; height: 100px; border: 2px solid var(--navy);
  }
  .address-lines { position: absolute; left: 478px; top: 246px; width: 204px; }
  .address-lines span { display: block; height: 1px; background: var(--rule); margin-bottom: 28px; }
</style>
</head>
<body>
<main class="canvas">

  <section class="postcard postcard--front" aria-label="Postcard front">
    <div class="band" style="top:0;width:697px;height:15px;"></div>

    <aside class="side-panel">
      <div class="brand" style="top:66px;"><span class="brand__dot"></span>Vantrell Chiropractic</div>
      <div class="headshot" role="img" aria-label="Headshot of the chiropractor in a dark polo shirt, arms crossed"></div>
      <div class="partner-bar" aria-label="Partner badges">
        <span class="partner-badge partner-badge--fmm" role="img" aria-label="Fluid Motion Methods badge"></span>
        <span class="partner-badge partner-badge--tide" role="img" aria-label="Tidebreaker partner badge"></span>
      </div>
    </aside>

    <h1 class="headline">
      If you've been in an auto accident,<br>
      <span class="headline__alert">the real damage</span><br>
      may not be this obvious
    </h1>

    <div class="scene" role="img" aria-label="Woman in a dark suit holding her neck and lower back beside a white car with a smashed front end"></div>

    <p class="no-cost">Not at fault? Your care will likely be at no cost to you.</p>

    <div class="contact-bar">
      <span class="contact-bar__phone">(555) 382-7146</span>
      <span class="contact-bar__web">www.vantrellchiro-example.com</span>
    </div>

    <div class="offer">
      <p class="offer__lead">Let us review your case.</p>
      <p class="offer__line">Schedule a Consult today</p>
      <p class="offer__line">and receive a FREE tube of Glacivo Pain Reliever <span class="offer__small">($10 value)</span>.</p>
    </div>
  </section>

  <section class="postcard postcard--back" aria-label="Postcard address side">
    <aside class="side-panel">
      <div class="band" style="top:0;width:212px;height:23px;"></div>
      <div class="brand" style="top:70px;"><span class="brand__dot"></span>Vantrell Chiropractic</div>
      <div class="disclaimer">
        <p class="disclaimer__title">This is an advertisement<br>for chiropractic services.</p>
        <p class="disclaimer__body">If you decide to purchase additional treatment,<br>you have the legal right to change your mind<br>within three days and receive a refund.</p>
      </div>
      <div class="band" style="top:428px;width:212px;height:25px;"></div>
    </aside>

    <div class="watermark" aria-hidden="true">Vantrell<br>Chiropractic</div>
    <div class="stamp-box" aria-label="Stamp area"></div>
    <div class="address-lines" aria-label="Address lines">
      <span></span><span></span><span></span><span></span><span></span>
    </div>
  </section>

</main>
</body>
</html>
```